Modern luxury trendy cosmetics label

Looking for a cosmetics packaging label design. We are looking for a professionel, modern and luxury look like Lorena Vasquel, Meadowkin Apothecary, Marigold Tessin, Gavin Albert Pruke, Zuna, Orvik + Dalle, Velumi, Sleepy Walrus, the plainfold, lumiere de sable.Name of product: Nordic Tulip Mask - Needle-Free Contour Ritual Ingredients that have scientific proof of anti aging: Cherry blossom extact, collegen, hyaluronic acid, coconut oil. Color of product itself: Pastel pink. Smell: Cherry blossom. Colors of label: simple and black and white or some subtle colors.

Target Market(s)

Women, luxury market, modern women, young and old women

Industry/Entity Type

Cosmetics

Font styles to use
Sans Serif

Colors

Designer to choose colors to be used in the design.

Requirements
Must have
• A modern look, professional, cosmetics, beauty, professional market, original

```html
<!DOCTYPE html>
<html lang="en">
<head>
<meta charset="utf-8">
<title>Nordic Tulip Mask Label</title>
<link rel="stylesheet" href="https://fonts.googleapis.com/css2?family=Abel&family=Kristi&display=swap">
<style>
  :root {
    --backdrop: #ececee;
    --label-white: #fff8fb;
    --blush: #f7cfe0;
    --blush-deep: #f2b3cf;
    --frame-pink: #ef98c0;
    --plum: #5b2352;
    --berry: #9a2d6d;
  }
  html, body {
    margin: 0;
    padding: 0;
    width: 900px;
    height: 1200px;
    overflow: hidden;
    background: var(--backdrop);
  }
  .label {
    position: absolute;
    left: 65px;
    top: 0;
    width: 769px;
    height: 1200px;
    background: var(--label-white);
    overflow: hidden;
    font-family: "Abel", "Arial Narrow", sans-serif;
    color: var(--plum);
  }
  .petal-field {
    position: absolute;
    inset: 0;
    background:
      radial-gradient(ellipse 60% 45% at 50% 45%, rgba(255,255,255,0.95), rgba(255,255,255,0) 70%),
      radial-gradient(ellipse 40% 30% at 85% 35%, rgba(247,207,224,0.7), rgba(247,207,224,0) 70%),
      radial-gradient(ellipse 40% 30% at 15% 75%, rgba(247,207,224,0.6), rgba(247,207,224,0) 70%),
      linear-gradient(180deg, var(--blush) 0%, #fdeef5 35%, #fdeef5 70%, var(--blush) 100%);
  }
  .frame {
    position: absolute;
    left: 0;
    top: 0;
  }
  .product-script {
    position: absolute;
    left: 150px;
    top: 150px;
    margin: 0;
    font-family: "Kristi", cursive;
    font-weight: 400;
    font-size: 200px;
    line-height: 1;
    color: var(--berry);
  }
  .product-name {
    position: absolute;
    right: 150px;
    top: 356px;
    margin: 0;
    font-size: 56px;
    font-weight: 400;
    line-height: 1;
    color: var(--plum);
  }
  .tagline {
    position: absolute;
    left: 0;
    right: 0;
    top: 585px;
    margin: 0;
    text-align: center;
    font-size: 60px;
    line-height: 78px;
    font-weight: 400;
  }
  .scent {
    position: absolute;
    left: 221px;
    width: 327px;
    top: 889px;
    height: 74px;
    border-top: 2px solid var(--plum);
    border-bottom: 2px solid var(--plum);
    display: flex;
    align-items: center;
    justify-content: center;
    font-size: 40px;
    letter-spacing: 1px;
  }
  .volume {
    position: absolute;
    left: 0;
    right: 0;
    top: 1003px;
    text-align: center;
    font-size: 33px;
  }
</style>
</head>
<body>
  <main class="label">
    <div class="petal-field" role="img" aria-label="Soft pink background of scattered cherry blossom petals"></div>
    <svg class="frame" width="769" height="1200" viewBox="0 0 769 1200" aria-hidden="true">
      <rect x="59" y="47" width="651" height="1108" fill="none" stroke="var(--frame-pink)" stroke-width="4"/>
      <rect x="76" y="64" width="617" height="1074" fill="none" stroke="var(--frame-pink)" stroke-width="2"/>
    </svg>
    <h1 class="product-script">Nordic</h1>
    <h2 class="product-name">Tulip Mask</h2>
    <p class="tagline">Needle-Free<br>Contour Ritual</p>
    <div class="scent">CHERRY BLOSSOM</div>
    <div class="volume">10 FL. OZ / 300 mLe</div>
  </main>
</body>
</html>
```